Notebook cover design for new launch friendship hamper

We need a cover design for an A5 notebook to fit in with our brand image for a newly launched gift hamper. The word "Notes" should appear on the cover in Futura font in yellow gold. The background colour should be navy blue (#00395F) and the pattern should be in peach (#E3C3B6) with possibly a small amount of yellow gold highlights.

Some examples of designs we like are attached, as well as a print file.

Target Market(s)

Women, 30-40

Requirements
Must have
• Navy blue background, peach pattern, a4 notebook size
Nice to have
• Gold highlights
Should not have
• Additional colours

```html
<!DOCTYPE html>
<html lang="en">
<head>
<meta charset="utf-8">
<title>Notes – Notebook Cover</title>
<link rel="stylesheet" href="https://fonts.googleapis.com/css2?family=Jost:wght@400&display=swap">
<style>
  :root {
    --paper: #ffffff;
    --sheet-edge: #8a8a8a;
    --navy: #00395F;
    --peach: #E3C3B6;
    --gold: #F5BF0A;
    --bronze: #C9A07A;
    --trim: #D6202A;
  }
  html, body {
    margin: 0;
    padding: 0;
    overflow: hidden;
    background: var(--paper);
  }
  .canvas {
    position: relative;
    width: 1200px;
    height: 887px;
    background: var(--paper);
    overflow: hidden;
  }
  .sheet-frame {
    position: absolute;
    left: 9px;
    top: 9px;
    width: 1180px;
    height: 867px;
    border: 1px solid var(--sheet-edge);
    box-sizing: border-box;
  }
  .cover {
    position: absolute;
    top: 53px;
    height: 781px;
    width: 509px;
    background: var(--navy);
    border: 1px solid var(--trim);
    box-sizing: border-box;
    overflow: hidden;
  }
  .cover--back {
    left: 53px;
    border-radius: 28px 0 0 28px;
  }
  .cover--front {
    left: 638px;
    border-radius: 0 28px 28px 0;
  }
  .ornament {
    position: absolute;
    bottom: 0;
    width: 356px;
    height: 482px;
    display: block;
  }
  .cover--back .ornament { right: 0; }
  .cover--front .ornament { left: 0; }
  .ornament-fill-top { stop-color: var(--peach); }
  .ornament-fill-bottom { stop-color: var(--bronze); }
  .cover-title {
    position: absolute;
    top: 53px;
    right: 55px;
    margin: 0;
    margin-right: -0.55em;
    font-family: "Jost", "Futura", sans-serif;
    font-weight: 400;
    font-size: 38px;
    line-height: 1;
    letter-spacing: 0.55em;
    color: var(--gold);
  }
</style>
</head>
<body>
  <main class="canvas">
    <div class="sheet-frame"></div>

    <section class="cover cover--back">
      <svg class="ornament" viewBox="0 0 356 482" role="img" aria-label="Peach filigree mandala pattern rising from the bottom spine edge">
        <defs>
          <linearGradient id="ornament-tone-back" x1="0" y1="0" x2="0" y2="1">
            <stop offset="0" class="ornament-fill-top"/>
            <stop offset="1" class="ornament-fill-bottom"/>
          </linearGradient>
        </defs>
        <ellipse cx="356" cy="352" rx="356" ry="352" fill="url(#ornament-tone-back)"/>
      </svg>
    </section>

    <section class="cover cover--front">
      <h1 class="cover-title">NOTES</h1>
      <svg class="ornament" viewBox="0 0 356 482" role="img" aria-label="Peach filigree mandala pattern rising from the bottom spine edge">
        <defs>
          <linearGradient id="ornament-tone-front" x1="0" y1="0" x2="0" y2="1">
            <stop offset="0" class="ornament-fill-top"/>
            <stop offset="1" class="ornament-fill-bottom"/>
          </linearGradient>
        </defs>
        <ellipse cx="0" cy="352" rx="356" ry="352" fill="url(#ornament-tone-front)"/>
      </svg>
    </section>
  </main>
</body>
</html>
```